Orva Business Card

we need a business card for flooring business called Orva Flooring, the design should be black and white. we have 2 locations

Halbrook Showroom
527 Kellerman Road,
Halbrook VIC 3187

Marlowe Showroom
462 Bramwell Hwy,
Marlowe VIC 3196

email : sales@orvaflooring.com.au
(03) 9471 2830

Please inform we sell , Laminate, Hybrid, Timber, carpet and commercial flooring

```html
<!DOCTYPE html>
<html lang="en">
<head>
<meta charset="utf-8">
<title>Orva Flooring – Business Card Concepts</title>
<link rel="stylesheet" href="https://fonts.googleapis.com/css2?family=Roboto:wght@300;400&display=swap">
<style>
  :root {
    --page: #9ba2a9;
    --card-black: #1b1b1b;
    --card-black-deep: #111;
    --card-brown: #231d17;
    --card-brown-deep: #16120e;
    --ink-light: #f2f2f2;
    --ink-dark: #111;
    --band: #ffffff;
    --rule: rgba(255,255,255,0.55);
  }
  * { box-sizing: border-box; margin: 0; padding: 0; }
  html, body { width: 1200px; height: 744px; overflow: hidden; }
  body {
    background: var(--page);
    font-family: "Roboto", Arial, sans-serif;
    color: var(--ink-light);
    position: relative;
  }
  .card {
    position: absolute;
    width: 306px;
    height: 186px;
    overflow: hidden;
  }
  .card-surface { position: absolute; inset: 0; }
  .card--black .card-surface { background: linear-gradient(160deg, var(--card-black), var(--card-black-deep)); }
  .card--brown .card-surface { background: linear-gradient(160deg, var(--card-brown), var(--card-brown-deep)); }

  /* Fronts */
  .front-name {
    position: absolute; inset: 0;
    display: flex; align-items: center; justify-content: center;
    font-weight: 300; font-size: 27px; letter-spacing: 2px;
    text-transform: uppercase; color: var(--ink-light);
  }

  /* Backs */
  .product-band {
    position: absolute; left: 35px; top: 11px; width: 271px; height: 43px;
    background: var(--band); color: var(--ink-dark);
  }
  .product-band .band-name {
    position: absolute; left: 8px; top: 0; height: 43px;
    display: flex; align-items: center;
    font-size: 7.5px; font-weight: 400; text-transform: uppercase; letter-spacing: 0.5px;
  }
  .product-band .band-heading {
    position: absolute; left: 71px; top: 4px; width: 198px;
    font-size: 12px; line-height: 14px; padding-bottom: 1px;
    border-bottom: 1.5px solid var(--ink-dark);
  }
  .product-band .band-list {
    position: absolute; left: 71px; top: 22px; width: 200px;
    font-size: 7.8px; line-height: 10.4px; white-space: nowrap;
  }
  .address {
    position: absolute; font-size: 8.4px; line-height: 12.3px; white-space: nowrap;
  }
  .divider { position: absolute; width: 1px; background: var(--rule); }
  .contact-row {
    position: absolute; left: 21px; display: flex; align-items: center; gap: 8px;
    font-size: 8.2px; white-space: nowrap;
  }
  .contact-item { display: flex; align-items: center; gap: 3px; }
  .contact-item svg { width: 9px; height: 8px; }

  .back-name {
    position: absolute; left: 0; right: 0; top: 22px; text-align: center;
    font-size: 9px; font-weight: 400; text-transform: uppercase; letter-spacing: 0.6px;
  }
  .offer {
    position: absolute; left: 178px; top: 75px; width: 112px;
    font-size: 8.4px; line-height: 12.3px;
  }
  .offer-heading { font-size: 10px; text-decoration: underline; margin-bottom: 1px; }
</style>
</head>
<body>

<svg width="0" height="0" style="position:absolute">
  <defs>
    <symbol id="icon-mail" viewBox="0 0 12 10">
      <rect x="0.5" y="0.5" width="11" height="9" fill="none" stroke="currentColor"/>
      <path d="M0.5 0.5 L6 5.5 L11.5 0.5" fill="none" stroke="currentColor"/>
    </symbol>
    <symbol id="icon-phone" viewBox="0 0 12 12">
      <path d="M2.5 0.8 L4.6 3.2 L3.4 4.6 C4.2 6.4 5.6 7.8 7.4 8.6 L8.8 7.4 L11.2 9.5 L9.6 11.2 C5 10.6 1.4 7 0.8 2.4 Z" fill="none" stroke="currentColor" stroke-width="0.9"/>
    </symbol>
  </defs>
</svg>

<!-- Concept 1 -->
<section class="card card--black card-front" style="left:66px; top:61px;">
  <div class="card-surface" role="img" aria-label="Dark black wood grain texture"></div>
  <div class="front-name">Orva Flooring</div>
</section>

<section class="card card--black card-back" style="left:386px; top:46px;">
  <div class="card-surface" role="img" aria-label="Dark black wood grain texture"></div>
  <div class="product-band">
    <div class="band-name">Orva Flooring</div>
    <div class="band-heading">Please inform we sell</div>
    <div class="band-list">Laminate flooring, Laminate flooring, Timber flooring,<br>Carpet and Commercial flooring</div>
  </div>
  <div class="address" style="left:21px; top:86px;">Halbrook Showroom<br>527 Kellerman Road,<br>Halbrook VIC 3187</div>
  <div class="divider" style="left:154px; top:80px; height:53px;"></div>
  <div class="address" style="left:197px; top:86px;">Marlowe Showroom<br>462 Bramwell Hwy,<br>Marlowe VIC 3196</div>
  <div class="contact-row" style="top:156px;">
    <span class="contact-item"><svg><use href="#icon-mail"/></svg>sales@orvaflooring.com.au</span>
    <span class="contact-item"><svg><use href="#icon-phone"/></svg>(03) 9471 2830</span>
  </div>
</section>

<!-- Concept 2 -->
<section class="card card--brown card-front" style="left:502px; top:269px;">
  <div class="card-surface" role="img" aria-label="Dark brown timber plank texture"></div>
  <div class="front-name">Orva Flooring</div>
</section>

<section class="card card--brown card-back" style="left:823px; top:289px;">
  <div class="card-surface" role="img" aria-label="Dark brown timber plank texture"></div>
  <div class="back-name">Orva Flooring</div>
  <div class="address" style="left:21px; top:67px;">Halbrook Showroom<br>527 Kellerman Road,<br>Halbrook VIC 3187</div>
  <div class="address" style="left:21px; top:115px;">Marlowe Showroom<br>462 Bramwell Hwy,<br>Marlowe VIC 3196</div>
  <div class="divider" style="left:154px; top:79px; height:54px;"></div>
  <div class="offer">
    <div class="offer-heading">Please inform we sell</div>
    Laminate flooring, Hybrid flooring, Timber flooring, carpet and commercial flooring
  </div>
  <div class="contact-row" style="top:155px;">
    <span class="contact-item"><svg><use href="#icon-mail"/></svg>sales@orvaflooring.com.au</span>
    <span class="contact-item"><svg><use href="#icon-phone"/></svg>(03) 9471 2830</span>
  </div>
</section>

<!-- Concept 3 -->
<section class="card card--black card-front" style="left:229px; top:501px;">
  <div class="card-surface" role="img" aria-label="Dark black wood grain texture"></div>
  <div class="front-name">Orva Flooring</div>
</section>

<section class="card card--black card-back" style="left:550px; top:521px;">
  <div class="card-surface" role="img" aria-label="Dark black wood grain texture"></div>
  <div class="product-band">
    <div class="band-name">Orva Flooring</div>
    <div class="band-heading">Please inform we sell</div>
    <div class="band-list">Laminate flooring, Laminate flooring, Timber flooring,<br>Carpet and Commercial flooring</div>
  </div>
  <div class="address" style="left:21px; top:86px;">Halbrook Showroom<br>527 Kellerman Road,<br>Halbrook VIC 3187</div>
  <div class="divider" style="left:154px; top:80px; height:53px;"></div>
  <div class="address" style="left:197px; top:86px;">Marlowe Showroom<br>462 Bramwell Hwy,<br>Marlowe VIC 3196</div>
  <div class="contact-row" style="top:156px;">
    <span class="contact-item"><svg><use href="#icon-mail"/></svg>sales@orvaflooring.com.au</span>
    <span class="contact-item"><svg><use href="#icon-phone"/></svg>(03) 9471 2830</span>
  </div>
</section>

</body>
</html>
```